Re-Design an adult education portal

I need support to re-design an adult education portal. Currently the customer has an incomplete website which should be prepared in a new format.
I have the idea how to realize, but I have no clue how to design it. The hard thing is to have a "beautiful" website with available logo and main color. I hope you can support me.

Name of Website: tovelu (tovelu.example)
Content: adult eduction for adult in safety at work, mountain climbing, dog school. various courses in different areas. But on old webpage is hard to find the different possibilities.
main color: Ral 6011 (green) -> #6C7C59
logo: you see on top of website the logo (2 dogs and a mountain with a colour gradient).

new website: for new webpage I decided to have a navigation for each section of education. In the main area I would like to have some pictures to give an idea what content is behind. At the moment it looks terrible, so I decided to use you as support for me to make the webpage prettier :). And maybe you have an better idea how to make it great. -> current state of new web page: https://tovelu.brisk-host.example/

Target Market(s)

adult eduction for adult in safety at work, mountain climbing, dog school

Number of Pages Required

1 page

Font styles to use
Serif
Sans Serif

Requirements
Must have
• As main color is set "Ral 6011" (green) -> #6C7C59

```html
<!DOCTYPE html>
<html lang="de">
<head>
<meta charset="utf-8">
<title>tovelu.example – Ausbildungs- und Kurspartner</title>
<link href="https://fonts.googleapis.com/css2?family=Josefin+Sans:wght@400;600&family=Oswald:wght@400;500&family=Libre+Caslon+Text&display=swap" rel="stylesheet">
<style>
:root{
  --green:#6C7C59;
  --dark:#353a42;
  --black:#0f100d;
  --grey:#ececec;
  --text:#1d1d1d;
  --white:#ffffff;
}
*{margin:0;padding:0;box-sizing:border-box}
html,body{width:1200px;height:3553px;overflow:hidden}
body{position:relative;background:var(--white);font-family:"Josefin Sans",sans-serif;color:var(--text)}
.abs{position:absolute}
.hero{left:0;top:0;width:1200px;height:710px;
  background:
    radial-gradient(ellipse 260px 420px at 120px 380px,rgba(235,242,220,.55),rgba(235,242,220,0) 70%),
    linear-gradient(100deg,#c3cfa9 0%,#a9b78c 18%,#8f9d72 30%,#66744f 37%,#1c1f16 41%,var(--black) 46%,var(--black) 100%);
  clip-path:polygon(0 0,100% 0,100% 607px,0 710px)}
.brand-box{left:112px;top:0;width:311px;height:163px;background:linear-gradient(180deg,#f4f2e4 0%,#e9e6c9 55%,#c9c79a 100%)}
.brand{left:112px;top:0;width:311px;height:163px;display:flex;align-items:center;justify-content:center;
  font-weight:600;font-size:38px;color:#1b1d16}
.nav{left:474px;top:33px;display:flex;gap:23px;font-size:16px;font-weight:600;color:var(--white)}
.hero-title{left:543px;top:245px;font-family:"Oswald",sans-serif;font-weight:500;font-size:40px;color:var(--white);letter-spacing:.3px}
.hero-text{left:543px;top:325px;width:542px;font-size:23px;line-height:31px;color:var(--white);text-align:justify;letter-spacing:.6px}
.dots{left:574px;top:621px;display:flex;gap:5px}
.dots span{width:13px;height:13px;border-radius:50%;background:var(--white)}
.dots span.on{background:var(--green)}
.serve-title{left:0;width:1200px;top:742px;text-align:center;font-family:"Libre Caslon Text",serif;font-size:44px;color:var(--text)}
.rule{height:3px;background:var(--green);width:72px}
.card{width:320px;height:420px}
.card .tab{position:absolute;left:37px;top:0;width:275px;height:273px;border-radius:12px}
.tab.g{background:var(--green)}.tab.d{background:var(--dark)}
.card .tab span{position:absolute;right:10px;top:34px;writing-mode:vertical-rl;font-family:"Oswald",sans-serif;font-size:14px;color:var(--white);letter-spacing:.3px}
.card .photo{position:absolute;left:0;top:33px;width:274px;height:274px;border-radius:0 12px 12px 12px}
.card .cap{position:absolute;left:0;top:325px;font-size:15px;line-height:20px;letter-spacing:.4px}
.cap b{font-weight:400;font-size:16px;display:block}
.about-bg{left:0;top:2175px;width:1200px;height:680px;background:var(--grey);clip-path:polygon(0 93px,100% 0,100% 590px,0 680px)}
.about-frame{left:122px;top:2331px;width:532px;height:403px;background:var(--green);border-radius:0 20px 20px 20px}
.about-photo{left:112px;top:2321px;width:533px;height:405px;border-radius:20px 0 20px 0;
  background:
    radial-gradient(ellipse 130px 160px at 170px 270px,rgba(205,190,170,.7),rgba(205,190,170,0) 70%),
    radial-gradient(ellipse 130px 160px at 390px 270px,rgba(220,215,210,.7),rgba(220,215,210,0) 70%),
    radial-gradient(ellipse 220px 120px at 420px 60px,rgba(70,120,200,.9),rgba(70,120,200,0) 75%),
    linear-gradient(180deg,#3e6ab0 0%,#6e5236 35%,#7a4f2c 60%,#4a3a2c 85%,#7a7570 100%)}
.about-title{left:698px;top:2314px;font-family:"Libre Caslon Text",serif;font-size:44px}
.about-text{left:698px;top:2407px;width:393px;font-size:15.6px;line-height:20.6px;text-align:justify;letter-spacing:.3px}
.goal-band{left:0;top:2765px;width:1200px;height:440px;background:var(--green);clip-path:polygon(0 90px,100% 0,100% 100%,0 100%)}
.goal{left:0;width:1200px;top:2895px;text-align:center;font-family:"Libre Caslon Text",serif;font-size:28px;line-height:38px;color:#eef0e8}
.btn{left:472px;top:2992px;width:259px;height:58px;border:2px solid var(--white);border-radius:30px;display:flex;align-items:center;justify-content:center;color:var(--white);font-size:25px;letter-spacing:1px}
.footer{left:0;top:3093px;width:1200px;height:460px;background:var(--dark);clip-path:polygon(0 79px,100% 0,100% 100%,0 100%)}
.foot-box{left:452px;top:3196px;width:312px;height:120px;background:linear-gradient(180deg,#f4f2e4 0%,#e9e6c9 55%,#c9c79a 100%)}
.foot-brand{left:452px;top:3196px;width:312px;height:120px;display:flex;align-items:center;justify-content:center;font-size:38px;font-weight:600;color:#1b1d16}
.contact{left:0;width:1200px;top:3396px;display:flex;justify-content:center;gap:52px;font-size:19px;color:var(--white);letter-spacing:.4px}
.contact span{display:flex;align-items:center;gap:6px}
.copy{left:0;width:1200px;top:3454px;text-align:center;font-size:19px;color:var(--white);letter-spacing:.4px}
</style>
</head>
<body>
<div class="abs hero" role="img" aria-label="Kletterer als Silhouette an einer dunklen Felswand vor hellgrünem Himmel"></div>
<div class="abs brand-box"></div>
<div class="abs brand">tovelu.example</div>
<nav class="abs nav"><span>Arbeitssicherheit</span><span>Erste Hilfe</span><span>Hundeschule</span><span>CZV</span><span>Bergausbildung</span><span>Tovelu</span></nav>
<h1 class="abs hero-title">Ihr Ausbildungs- und Kurspartner</h1>
<p class="abs hero-text">Wir bieten Ihren Wünschen entsprechende Ausbildungen, zielorientiert und Ihrem Können und Wissen angepasst.</p>
<div class="abs dots"><span></span><span class="on"></span><span></span></div>

<h2 class="abs serve-title">WE SERVE</h2>
<div class="abs rule" style="left:564px;top:802px"></div>

<div class="abs card" style="left:109px;top:862px"><div class="tab g"><span>STAPLERKURSE</span></div><div class="photo" role="img" aria-label="Frau am Schreibtisch vor Kamera" style="background:radial-gradient(ellipse 90px 110px at 150px 130px,#a98a72,rgba(169,138,114,0) 70%),radial-gradient(ellipse 60px 50px at 210px 230px,#2a2a2a,rgba(42,42,42,0) 80%),linear-gradient(135deg,#eceae5,#d8d5cf 60%,#bfb8ad)"></div><div class="cap"><b>STAPLERKURSE</b>Grundausbildung</div></div>
<div class="abs card" style="left:444px;top:862px"><div class="tab d"><span>PSAGA</span></div><div class="photo" role="img" aria-label="Person in Schutzanzug mit Kanistern" style="background:radial-gradient(ellipse 80px 120px at 160px 120px,#f4f5f7,rgba(244,245,247,0) 75%),radial-gradient(ellipse 60px 40px at 230px 250px,#3a6fc4,rgba(58,111,196,0) 80%),radial-gradient(ellipse 50px 40px at 50px 250px,#6fbf3a,rgba(111,191,58,0) 80%),linear-gradient(135deg,#c9a983,#d8cdbc 55%,#9a8c7c)"></div><div class="cap"><b>PSAgA</b>Persönliche Schutzausrüstung<br>gegen Absturz (PSAgA)</div></div>
<div class="abs card" style="left:778px;top:862px"><div class="tab g"><span>HUBARBEITSBÜHNE</span></div><div class="photo" role="img" aria-label="Hafenkran vor blauem Himmel" style="background:radial-gradient(ellipse 110px 90px at 140px 170px,#b3a46a,rgba(179,164,106,0) 75%),linear-gradient(160deg,#1f3042,#3c6585 45%,#2a3b4a)"></div><div class="cap"><b>HUBARBEITSBÜHNE</b>Bedienerschulung<br>Bedienerschulung / CZV</div></div>

<div class="abs card" style="left:109px;top:1291px"><div class="tab d"><span>HUNDESCHULE</span></div><div class="photo" role="img" aria-label="Hund mit Rucksack auf Wanderweg" style="background:radial-gradient(ellipse 70px 90px at 130px 150px,#c9a474,rgba(201,164,116,0) 75%),radial-gradient(ellipse 40px 40px at 100px 160px,#d9862f,rgba(217,134,47,0) 80%),linear-gradient(110deg,#9a9892 0%,#85827a 45%,#5a6a3a 75%,#3f4a2a)"></div><div class="cap"><b>HUNDESCHULE</b>Welpenförderung Agility Mantrailing</div></div>
<div class="abs card" style="left:444px;top:1291px"><div class="tab g"><span>NOTHELFER</span></div><div class="photo" role="img" aria-label="Stethoskop an grüner Arztkleidung" style="background:radial-gradient(ellipse 40px 40px at 90px 190px,#f4552e,rgba(244,85,46,0) 80%),linear-gradient(135deg,#f1f1f1 0%,#e8efec 25%,#8fd3b8 45%,#6cc2a4 100%)"></div><div class="cap"><b>NOTHELFER</b>Auffrischungskurs<br>Gutschein für Fahrstunden bei xyz</div></div>
<div class="abs card" style="left:778px;top:1291px"><div class="tab d"><span>SANITÄTSSCHULUNG</span></div><div class="photo" role="img" aria-label="Person in Schutzanzug reinigt Kühlschrank" style="background:radial-gradient(ellipse 30px 30px at 80px 150px,#4f86d6,rgba(79,134,214,0) 80%),radial-gradient(ellipse 90px 140px at 200px 150px,#f6f6f6,rgba(246,246,246,0) 75%),linear-gradient(135deg,#5f5a56,#9a948e 35%,#e4e4e4 60%,#d9dce0)"></div><div class="cap"><b>SANITÄTSSCHULUNG</b>Auffrischungskurs</div></div>

<div class="abs card" style="left:109px;top:1720px"><div class="tab g"><span>RVS AGD</span></div><div class="photo" role="img" aria-label="Regionalzug auf Gleisen" style="background:radial-gradient(ellipse 60px 30px at 190px 120px,#c8e33a,rgba(200,227,58,0) 80%),radial-gradient(ellipse 120px 90px at 150px 130px,#f0f0ee,rgba(240,240,238,0) 75%),linear-gradient(180deg,#c9d8e8 0%,#dfe6ec 45%,#8c8a84 80%,#6b6a65)"></div><div class="cap"><b>RVS AGD</b>Auffrischungskurs</div></div>
<div class="abs card" style="left:444px;top:1720px"><div class="tab d"><span>CZV</span></div><div class="photo" role="img" aria-label="Lastwagen einer Fahrschule" style="background:radial-gradient(ellipse 110px 120px at 140px 130px,#15171a,rgba(21,23,26,0) 80%),linear-gradient(170deg,#4f7fc4 0%,#6d92c9 30%,#7a8d5a 65%,#8a8c88)"></div><div class="cap"><b>CZV</b>Berufsfahrer Weiterbildung<br>Arbeits- und Ruhezeitverordnung<br>Eco-Drive Fahrzeugtechnik</div></div>
<div class="abs card" style="left:778px;top:1720px"><div class="tab g"><span>BERGAUSBILDUNG</span></div><div class="photo" role="img" aria-label="Wanderer im Gebirge" style="background:linear-gradient(180deg,#c9ced3 0%,#b6bcc0 25%,#6f7466 40%,#8b7a52 65%,#7a6140 85%,#8a8680)"></div><div class="cap"><b>BERGAUSBILDUNG</b>Bergklettern<br>Touren<br>Erste Hilfe</div></div>

<div class="abs about-bg"></div>
<div class="abs about-frame"></div>
<div class="abs about-photo" role="img" aria-label="Zwei Personen mit drei Hunden im Herbstwald"></div>
<h2 class="abs about-title">Über uns</h2>
<div class="abs rule" style="left:698px;top:2374px"></div>
<p class="abs about-text">In meiner Beruflichen Laufbahn erlebte ich immer wieder Situationen, welche in mir die Idee reifen liessen, jedem interessierten Menschen ein Grundwissen zukommen zu lassen, welches ihn bei einer Notsituation richtig und mit der nötigen Ruhe reagieren lässt. Das Zusammenlegen &amp; Kombinieren von Wissen und Fertigkeiten der verschiedenen Fachbereiche gibt dem Menschen Sicherheit und Vertrauen in seinem Handeln. Aus eigener Erfahrung hat sich gezeigt: je professioneller man auf Grenzsituationen vorbereitet ist, desto sicherer und erfolgreicher kann eine Notfallsituation gemeistert und sogar Leben gerettet werden.</p>

<div class="abs goal-band"></div>
<p class="abs goal">Ziel: Professionelles, sicheres und ruhiges<br>Agieren in allen Situationen!</p>
<div class="abs btn">OUR COURSE</div>

<div class="abs footer"></div>
<div class="abs foot-box"></div>
<div class="abs foot-brand">tovelu.example</div>
<div class="abs contact">
  <span><svg width="14" height="18" viewBox="0 0 14 18"><path d="M7 0a7 7 0 0 0-7 7c0 5 7 11 7 11s7-6 7-11a7 7 0 0 0-7-7zm0 10a3 3 0 1 1 0-6 3 3 0 0 1 0 6z" fill="#fff"/></svg>Lindenweg 27, CH-3999 Musterdorf</span>
  <span><svg width="17" height="17" viewBox="0 0 24 24"><path d="M6.6 10.8a15 15 0 0 0 6.6 6.6l2.2-2.2c.3-.3.7-.4 1-.2 1.1.4 2.3.6 3.6.6.6 0 1 .4 1 1V20c0 .6-.4 1-1 1A17 17 0 0 1 3 4c0-.6.4-1 1-1h3.5c.6 0 1 .4 1 1 0 1.3.2 2.5.6 3.6.1.3 0 .7-.2 1z" fill="#fff"/></svg>Telefon: +41 79 000 12 34</span>
  <span><svg width="24" height="16" viewBox="0 0 24 16"><rect x="1" y="1" width="22" height="14" fill="#fff"/><path d="M1 1l11 8 11-8M1 15l8-7M23 15l-8-7" stroke="#353a42" stroke-width="1.6" fill="none"/></svg>E-Mail: info@tovelu.example</span>
</div>
<p class="abs copy">© Copyright bei tovelu.example 2021</p>
</body>
</html>
```